Commercial janitorial company looking for a fresh and modern website design

We need a new website design for our Edmonton, Alberta-based commercial cleaning company called Brevint Upkeep Limited. We have been providing services throughout Alberta for over 50 years, and have a strong customer-oriented service reputation. We are working to re-brand our image and the next crucial piece of that is an informative, simple, and modern website. We provide full service office and industrial cleaning, periodic services, and basic building maintenance, with a focus on being a 'silent partner' for our clients, allowing them to focus on their core business services. We are committed to the highest safety standards and industry best practices for productivity, employing environmentally friendly products practices in all our locations.

We would like a visually pleasing, easy-to-navigate website structure that provides clear communication through imagery and minimal text.

Target Market(s)

Commercial businesses

Industry/Entity Type

It Company

Font styles to use
Other font styles liked:
• Segoe (similar to our logo's font)

Requirements
Must have
• We would like the landing page to be extremely straightforward, with minimal scrolling required, and minimal text presence. We will likely have up to 5 sub-menus / pages, leading off from the main landing page. These pages will have further text on them, supplying further information. We would prefer their location on the top of the screen to be locked or in some way present during any page scrolling.
• Our logos are also available in eps, pdf, ai formats.
Nice to have
• Some websites that we like the presentation of include:
• tonvaleworks.hr
• quarnbridgeads.com
• rqo.com
• volmira.com
• usetaskly.com
• pacewell.com

```html
<!DOCTYPE html>
<html lang="en">
<head>
<meta charset="utf-8">
<title>Brevint Upkeep Limited</title>
<link href="https://fonts.googleapis.com/css2?family=Open+Sans:ital,wght@0,300;0,400;0,600;0,700;1,400;1,600&display=swap" rel="stylesheet">
<style>
:root{
  --blue:#1a96d8;
  --green:#3aaa35;
  --green-light:#5ccd3f;
  --green-btn:#3aa635;
  --ink:#333;
  --muted:#777;
  --faint:#999;
  --bg-soft:#f4f4f6;
  --dark:#2b2b2b;
  --white:#fff;
  --line:#ddd;
}
*{box-sizing:border-box;margin:0;padding:0}
html,body{width:720px;height:1200px;overflow:hidden}
body{font-family:"Open Sans",Arial,sans-serif;color:var(--ink);background:var(--white);position:relative}
a{color:inherit;text-decoration:none}

/* header */
.site-header{position:absolute;left:0;top:0;width:720px;height:48px;background:var(--white)}
.brand{position:absolute;left:48px;top:12px;display:flex;align-items:center;gap:6px;font-size:15px;font-weight:400;color:#555;letter-spacing:.5px}
.brand-dot{width:20px;height:20px;border-radius:50%;background:var(--blue)}
.main-nav{position:absolute;left:175px;top:20px;display:flex;gap:22px;font-size:7.5px;color:#555}
.main-nav .active{color:var(--blue)}
.header-phone{position:absolute;left:588px;top:18px;display:flex;align-items:center;gap:6px;color:var(--green);font-size:9px;font-weight:600;text-decoration:underline}

/* hero */
.hero{position:absolute;left:0;top:48px;width:720px;height:288px}
.hero-photo{position:absolute;inset:0;background:linear-gradient(100deg,#5b5d60 0%,#8a7a6e 30%,#c9622f 42%,#7c7f82 60%,#4e5154 100%)}
.hero-shade{position:absolute;inset:0;background:rgba(20,20,20,.35)}
.hero-title{position:absolute;left:0;width:720px;top:100px;text-align:center;color:var(--white);font-size:18px;font-weight:400}
.hero-sub{position:absolute;left:0;width:720px;top:120px;text-align:center;color:var(--white);font-size:11.5px;line-height:14px}
.btn-primary{position:absolute;left:288px;top:164px;width:67px;height:19px;background:var(--blue);color:var(--white);font-size:8px;display:flex;align-items:center;justify-content:center}
.btn-outline{position:absolute;left:365px;top:164px;width:67px;height:19px;border:1px solid var(--white);color:var(--white);font-size:8px;display:flex;align-items:center;justify-content:center}

/* stats */
.stats-bar{position:absolute;left:0;top:336px;width:720px;height:57px;background:var(--white);box-shadow:0 2px 3px rgba(0,0,0,.05)}
.stat-number{position:absolute;left:93px;top:10px;font-size:30px;font-weight:400;font-style:italic;color:#222}
.stat-label{position:absolute;left:132px;top:19px;font-size:7px;color:#666;line-height:11px}
.stat-label strong{font-size:8.5px;color:#333;font-weight:600}
.stat-divider{position:absolute;left:255px;top:12px;height:34px;border-left:1px dotted #aaa}
.mission-icon{position:absolute;left:276px;top:21px}
.mission{position:absolute;left:307px;top:17px;font-size:7px;color:#555;line-height:11.5px}
.mission em{font-weight:600;color:#333}

/* services */
.services{position:absolute;left:0;top:393px;width:720px;height:407px;background:var(--bg-soft)}
.section-title{position:absolute;left:0;width:720px;top:24px;text-align:center;color:var(--blue);font-size:17px;font-weight:700}
.section-sub{position:absolute;left:0;width:720px;top:49px;text-align:center;color:#666;font-size:8px}
.service-card{position:absolute;top:77px;width:122px;height:120px;overflow:hidden}
.service-photo{position:absolute;inset:0}
.service-caption{position:absolute;left:0;bottom:0;width:100%;height:24px;background:rgba(30,30,30,.85);color:var(--white);font-size:8.5px;font-weight:600;padding:6px 9px}
.service-caption.open{height:43px}
.service-link{display:flex;align-items:center;gap:3px;color:var(--blue);font-size:7px;font-weight:400;margin-top:6px}
.sectors-rule{position:absolute;top:229px;height:1px;background:var(--line)}
.sectors-label{position:absolute;left:0;width:720px;top:224px;text-align:center;font-size:8px;color:#888}
.sector{position:absolute;top:256px;width:110px;text-align:center;font-size:8.5px;color:#555}
.sector-ring{width:60px;height:60px;border-radius:50%;border:1px solid var(--blue);margin:0 auto 12px;display:flex;align-items:center;justify-content:center;background:var(--white)}
.sector.active .sector-ring{background:var(--blue)}
.sector.active{color:#333;font-weight:600}
.carousel-arrow{position:absolute;top:285px}
.btn-dark{position:absolute;left:329px;top:361px;width:62px;height:18px;background:var(--dark);color:var(--white);font-size:7.5px;display:flex;align-items:center;justify-content:center}

/* cta band */
.why{position:absolute;left:0;top:800px;width:360px;height:156px;background:var(--green);color:var(--white)}
.why h2{position:absolute;left:94px;top:26px;font-size:14.5px;font-weight:700;line-height:20px}
.why p{position:absolute;left:94px;top:58px;font-size:11.5px;line-height:14px;width:236px;font-weight:400}
.why .btn-dark{left:94px;top:109px;width:76px}
.join{position:absolute;left:360px;top:800px;width:360px;height:156px;background:var(--green-light);color:var(--white)}
.join h2{position:absolute;left:31px;top:26px;font-size:14.5px;font-weight:700;line-height:20px}
.join .lead{position:absolute;left:31px;top:46px;font-size:8px;line-height:11px}
.zip-input{position:absolute;left:31px;top:62px;width:139px;height:19px;background:var(--white);color:#9a9;font-size:7px;font-style:italic;padding:5px 7px}
.zip-btn{position:absolute;left:170px;top:62px;width:96px;height:19px;background:var(--green-btn);font-size:8px;font-weight:600;display:flex;align-items:center;justify-content:center}
.join .help{position:absolute;left:31px;top:96px;font-size:7px;line-height:10.5px}
.join .help b{font-size:8px;font-weight:700}
.join .help .call{font-style:italic;font-weight:700}
.join .help u{font-weight:700}

/* footer */
.footer-brand{position:absolute;left:0;width:720px;top:988px;display:flex;justify-content:center;align-items:center;gap:5px;font-size:11px;color:#555;letter-spacing:.4px}
.footer-brand .brand-dot{width:16px;height:16px;background:#888}
.footer-rule{position:absolute;top:996px;height:1px;background:var(--line)}
.footer-col{position:absolute;top:1024px;width:160px}
.footer-col h3{font-size:8.5px;font-weight:600;color:#444;margin-bottom:9px}
.footer-links li{list-style:none;font-size:7px;color:var(--faint);line-height:14px}
.footer-links .current{color:var(--blue)}
.footer-text{font-size:7px;color:var(--faint);line-height:9.5px}
.email-input{width:137px;height:17px;border:1px solid var(--line);font-size:6.5px;color:#aaa;font-style:italic;padding:4px 7px;margin-top:8px}
.btn-green{width:60px;height:17px;background:var(--green-btn);color:var(--white);font-size:7.5px;display:flex;align-items:center;justify-content:center;margin-top:5px}
.footer-phone{display:flex;align-items:center;gap:4px;color:var(--green);font-size:11.5px;margin-top:10px}
.social{display:flex;gap:4px;margin-top:13px}
.social span{width:15px;height:15px;background:#8a9aa6}
.back-top{position:absolute;left:656px;top:1128px;text-align:center;font-size:6px;color:#666;font-style:italic;text-decoration:underline}
.footer-base{position:absolute;left:94px;width:532px;top:1150px;border-top:1px solid var(--line)}
.copyright{position:absolute;left:94px;top:1172px;font-size:7px;color:#555}
.legal{position:absolute;left:458px;top:1172px;font-size:7px;color:var(--faint);word-spacing:1px}
</style>
</head>
<body>

<header class="site-header">
  <div class="brand"><span class="brand-dot"></span>Brevint</div>
  <nav class="main-nav">
    <a>What We Do? &#8964;</a>
    <a>Where We Operate? &#8964;</a>
    <a class="active">Who We Are?</a>
    <a>Work With Us</a>
  </nav>
  <div class="header-phone">
    <svg width="11" height="11" viewBox="0 0 24 24"><circle cx="12" cy="12" r="10.5" fill="none" stroke="#3aaa35" stroke-width="2"/><path d="M8 6.5l2 2.5-1.2 1.5c.8 1.7 2 2.9 3.7 3.7l1.5-1.2 2.5 2-1.2 1.8c-4-.5-7.8-4.3-8.3-8.3z" fill="#3aaa35"/></svg>
    1.800.555.0142
  </div>
</header>

<section class="hero">
  <div class="hero-photo" role="img" aria-label="Cleaning staff working in a bright office lobby with orange sofas"></div>
  <div class="hero-shade"></div>
  <h1 class="hero-title">Brevint works as 'silent partner' for all clients!</h1>
  <p class="hero-sub">Focus on your core Business Services as we commit the Highest safety standards<br>&amp; Industry best practices for all Client locations.</p>
  <a class="btn-primary">Learn More</a>
  <a class="btn-outline">Contact Us</a>
</section>

<section class="stats-bar">
  <div class="stat-number">50</div>
  <div class="stat-label">Year of Commercial Cleaning<br><strong>Experiance</strong>
    <svg width="8" height="8" viewBox="0 0 10 10"><rect x=".5" y=".5" width="9" height="9" fill="none" stroke="#3aaa35"/><path d="M2 5l2 2 5-5" fill="none" stroke="#3aaa35" stroke-width="1.4"/></svg>
  </div>
  <div class="stat-divider"></div>
  <svg class="mission-icon" width="24" height="14" viewBox="0 0 24 14"><circle cx="6" cy="8" r="4.5" fill="none" stroke="#222" stroke-width="2"/><circle cx="18" cy="8" r="4.5" fill="none" stroke="#222" stroke-width="2"/><rect x="9" y="4" width="6" height="3" fill="#222"/></svg>
  <div class="mission">
    - To provide the highest quality cleaning services, based on <em>clearly laid out expectations.</em><br>
    - To be the community's <em>leading service provider</em> and employer of choice.
  </div>
</section>

<section class="services">
  <h2 class="section-title">What We Do?</h2>
  <p class="section-sub">One of the largest providers of cleaning services in Alberta, CA</p>

  <div class="service-card" style="left:94px">
    <div class="service-photo" role="img" aria-label="Office cleaner mopping a lounge area" style="background:linear-gradient(160deg,#d8dadc,#b86a3c 60%,#7d7f82)"></div>
    <div class="service-caption">Office Cleaning</div>
  </div>
  <div class="service-card" style="left:231px">
    <div class="service-photo" role="img" aria-label="Worker in coveralls cleaning an industrial facility" style="background:linear-gradient(160deg,#6e7378,#a9adb1 55%,#55595d)"></div>
    <div class="service-caption open">Industrial Cleaning
      <div class="service-link"><svg width="7" height="7" viewBox="0 0 10 10"><circle cx="5" cy="5" r="5" fill="#1a96d8"/><path d="M4 3l2 2-2 2" stroke="#fff" fill="none" stroke-width="1.3"/></svg>Learn More</div>
    </div>
  </div>
  <div class="service-card" style="left:367px">
    <div class="service-photo" role="img" aria-label="Window cleaning gondola on a glass tower" style="background:linear-gradient(150deg,#9dc3e3,#3f6f9a 60%,#2b4a68)"></div>
    <div class="service-caption">Periodic Services</div>
  </div>
  <div class="service-card" style="left:504px">
    <div class="service-photo" role="img" aria-label="Technician on a ladder maintaining a building wall" style="background:linear-gradient(150deg,#b7d5ee,#e4e6e8 55%,#8e9296)"></div>
    <div class="service-caption">Building Maintenance</div>
  </div>

  <div class="sectors-rule" style="left:94px;width:210px"></div>
  <div class="sectors-rule" style="left:416px;width:210px"></div>
  <div class="sectors-label">Where We Operate?</div>

  <svg class="carousel-arrow" style="left:67px" width="12" height="22" viewBox="0 0 12 22"><path d="M11 1L1 11l10 10" fill="none" stroke="#aaa" stroke-width="1.2"/></svg>
  <svg class="carousel-arrow" style="left:640px" width="12" height="22" viewBox="0 0 12 22"><path d="M1 1l10 10L1 21" fill="none" stroke="#444" stroke-width="1.2"/></svg>

  <div class="sector" style="left:100px">
    <div class="sector-ring"><svg width="28" height="28" viewBox="0 0 28 28" fill="#1a96d8"><circle cx="19" cy="6" r="3"/><rect x="16" y="10" width="6" height="9"/><rect x="2" y="13" width="13" height="3"/><rect x="4" y="16" width="9" height="8"/><rect x="17" y="19" width="3" height="6"/><rect x="3" y="8" width="7" height="5"/></svg></div>
    Office Facilities
  </div>
  <div class="sector active" style="left:237px">
    <div class="sector-ring"><svg width="28" height="28" viewBox="0 0 28 28" fill="#fff"><path d="M14 3l1 2h-2z"/><path d="M7 12a7 6 0 0114 0z"/><rect x="5" y="12" width="18" height="2"/><rect x="6" y="15" width="2" height="7"/><rect x="10" y="15" width="2" height="7"/><rect x="14" y="15" width="2" height="7"/><rect x="18" y="15" width="2" height="7"/><rect x="4" y="22" width="20" height="2"/></svg></div>
    Government Facilities
  </div>
  <div class="sector" style="left:374px">
    <div class="sector-ring"><svg width="28" height="28" viewBox="0 0 28 28" fill="#1a96d8"><path d="M4 24V14l5-2v12z"/><path d="M11 24V8l7-3v19z"/><path d="M20 24V4l4-1v21z"/></svg></div>
    Retail Facilities
  </div>
  <div class="sector" style="left:510px">
    <div class="sector-ring"><svg width="28" height="28" viewBox="0 0 28 28" fill="#1a96d8"><rect x="7" y="4" width="3" height="8"/><rect x="17" y="4" width="3" height="8"/><path d="M4 12h20v12H4z"/><rect x="7" y="17" width="3" height="3" fill="#fff"/><rect x="12" y="17" width="3" height="3" fill="#fff"/><rect x="17" y="17" width="3" height="3" fill="#fff"/></svg></div>
    Industrial Facilities
  </div>

  <a class="btn-dark">Read More</a>
</section>

<section class="why">
  <h2>Why Work With Brevint !</h2>
  <p>A Fully Devoted to local economic growth and employing a &nbsp;eam that is highly approachable &amp; family-oriented!</p>
  <a class="btn-dark">Approach Now</a>
</section>

<section class="join">
  <h2>Want to work with us?</h2>
  <p class="lead">Get Started with Brevint Upkeep Limited</p>
  <div class="zip-input">Enter your Zip Code</div>
  <a class="zip-btn">Find My Location</a>
  <p class="help"><b>Not sure where to go?</b><br><span class="call">Just call us at <u>1.800.555.0142</u> Brevint,</span><br>we're here to help.</p>
</section>

<footer>
  <div class="footer-rule" style="left:94px;width:210px"></div>
  <div class="footer-rule" style="left:416px;width:210px"></div>
  <div class="footer-brand"><span class="brand-dot"></span>BREVINT</div>

  <div class="footer-col" style="left:94px">
    <h3>Quick Links</h3>
    <ul class="footer-links">
      <li>About Us</li><li>Our Services</li><li class="current">Our Sectors</li><li>Investor Relations</li><li>Contact</li><li>Careers</li>
    </ul>
  </div>
  <div class="footer-col" style="left:276px">
    <h3>Subscribe Us</h3>
    <p class="footer-text">Get the latest news from Brevint, right in<br>your inbox</p>
    <div class="email-input">Enter Your Email</div>
    <a class="btn-green">Subscribe</a>
  </div>
  <div class="footer-col" style="left:458px">
    <h3>Contact Info</h3>
    <p class="footer-text">Harlow Street 14, 3rd floor, Edmonton<br>Canada T5J 2R4</p>
    <div class="footer-phone">
      <svg width="13" height="13" viewBox="0 0 24 24"><circle cx="12" cy="12" r="10.5" fill="none" stroke="#3aaa35" stroke-width="2"/><path d="M8 6.5l2 2.5-1.2 1.5c.8 1.7 2 2.9 3.7 3.7l1.5-1.2 2.5 2-1.2 1.8c-4-.5-7.8-4.3-8.3-8.3z" fill="#3aaa35"/></svg>
      1.800.555.0142
    </div>
    <p class="footer-text" style="margin-top:2px">support@brevint.com</p>
    <div class="social"><span></span><span></span><span></span><span></span><span></span></div>
  </div>

  <div class="back-top">
    <svg width="9" height="9" viewBox="0 0 10 10"><path d="M5 1v8M1.5 4.5L5 1l3.5 3.5" stroke="#3aaa35" stroke-width="1.8" fill="none"/></svg><br>Back to Top
  </div>

  <div class="footer-base"></div>
  <p class="copyright">Copyright © 2016, Brevint Upkeep Ltd. Canada</p>
  <p class="legal">Privacy Policy &nbsp;/&nbsp; T&amp;C's &nbsp;/&nbsp; Site Map &nbsp;/&nbsp; FAQ's</p>
</footer>

</body>
</html>
```